Bref créative
leap fern boots homepage
selling leap fern boots and glide to live book
Apparel
www.leapfernboots-demo.com (not live)
Leap fern boots...leap home to earth. Runners are running barefoot more than ever and leapfern boots is the minimal shoe that will help the runner transition back to nature.. Running Barefoot!
About us: Leap Fern Boots are created to get the runner back to nature. These shoes are designed to transition the runner from running shoes to leap fern boots and eventually running barefoot. Leap Fern Boots are lightweight and developed to handle the terrain and pavement as if you weren’t wearing any shoes at all. The Barefoot running alternative!
Natural, Eco Friendly, Scientific,
approved logo is attached
http://www.quilvantor.com/contests/leap-fern-boots/users/TOBYstudio
I own the mov
http://www.pelmarclips.com/stock-video-5820913-neon-sprint-figure-cycle.php
Black
White/ beige
left side
http://www.vekzo.org/
http://www.lum.org/
http://www.pelmarclips.com/
I have 105 credits at Pel mar clips.com feel free to browse and use pictures in front page. Purpose of site is to sell a book live to glide and leapfernboots. I like banners, for example the banner shoes a pair of shoes and moves on to the next banner showing the book with buy now buttons. mov file available as well. I will have a jpeg of shoes later...for now just find a pair and use that and we will switch it out

```html
<!DOCTYPE html>
<html lang="en">
<head>
<meta charset="utf-8">
<title>Leap Fern Boots</title>
<link href="https://fonts.googleapis.com/css2?family=Arimo:wght@400;700&family=Roboto+Condensed:ital,wght@1,700&display=swap" rel="stylesheet">
<style>
  :root {
    --bg-dark: #0f0f0f;
    --bg-mid: #1c1c1c;
    --footer: #070707;
    --green: #8cc63f;
    --green-light: #b4e06a;
    --green-dark: #4f8a16;
    --text: #d8d8d8;
    --text-dim: #8a8a8a;
    --white: #ffffff;
    --photo-light: #e4e4e4;
    --photo-dark: #8d8d8d;
  }
  * { margin: 0; padding: 0; box-sizing: border-box; }
  html, body { width: 1200px; height: 967px; overflow: hidden; }
  body {
    position: relative;
    background: radial-gradient(ellipse at 50% 40%, var(--bg-mid) 0%, var(--bg-dark) 70%);
    font-family: "Arimo", Arial, sans-serif;
    color: var(--text);
  }
  .heading {
    position: absolute;
    font-family: "Roboto Condensed", "Arial Narrow", sans-serif;
    font-style: italic;
    font-weight: 700;
    color: var(--green);
    text-transform: uppercase;
    letter-spacing: -0.3px;
  }
  .copy {
    position: absolute;
    font-size: 11.5px;
    line-height: 15px;
    color: var(--text);
  }

  .brand {
    position: absolute; left: 191px; top: 5px; width: 240px; height: 81px;
    background: var(--white); border: 2px solid #cfcfcf;
    display: flex; align-items: center; justify-content: center; gap: 10px;
  }
  .brand-mark { width: 18px; height: 18px; background: var(--green); }
  .brand-name {
    font-family: "Roboto Condensed", sans-serif; font-style: italic; font-weight: 700;
    font-size: 26px; color: #1a1a1a; text-transform: uppercase;
  }

  .main-nav {
    position: absolute; left: 196px; top: 102px; width: 802px; height: 39px;
    border-radius: 5px; border: 2px solid var(--green-light);
    background: linear-gradient(var(--green-light), var(--green) 45%, var(--green-dark));
    display: flex; align-items: center; padding-left: 12px;
  }
  .main-nav a {
    color: var(--white); text-decoration: none; font-size: 11px; font-weight: 700;
    text-transform: uppercase; padding: 0 20px; height: 100%;
    display: flex; align-items: center;
    border-right: 1px solid rgba(0,0,0,0.25);
  }
  .main-nav a:last-child { border-right: 0; }

  .buy-now {
    position: absolute; left: 358px; top: 434px; width: 120px; height: 29px;
    background: #000; color: var(--white); font-family: "Roboto Condensed", sans-serif;
    font-style: italic; font-weight: 700; font-size: 13px; text-transform: uppercase;
    display: flex; align-items: center; justify-content: center;
  }

  .frame { position: absolute; background: var(--white); padding: 6px; overflow: hidden; }
  .photo { width: 100%; height: 100%; background: radial-gradient(ellipse at 45% 55%, var(--photo-dark), var(--photo-light) 75%); }
  .ribbon { position: absolute; top: 0; right: 0; overflow: visible; }

  .hero-frame { left: 502px; top: 209px; width: 491px; height: 254px; padding: 12px; overflow: visible; }
  .thumb { top: 517px; width: 178px; height: 97px; overflow: visible; }

  .site-footer {
    position: absolute; left: 0; top: 923px; width: 1200px; height: 44px;
    background: var(--footer); color: var(--text-dim); font-size: 10px;
    display: flex; align-items: center; justify-content: center;
  }
</style>
</head>
<body>

<div class="brand">
  <span class="brand-mark"></span>
  <span class="brand-name">Leap Fern Boots</span>
</div>

<nav class="main-nav">
  <a href="#">Home</a>
  <a href="#">About Us</a>
  <a href="#">Our Services</a>
  <a href="#">Testimonials</a>
  <a href="#">Contact Us</a>
</nav>

<h2 class="heading" style="left:204px; top:240px; font-size:21px;">Fern Boots</h2>
<p class="copy" style="left:204px; top:273px; width:272px; height:120px; overflow:hidden;">Lorem ipsum dolor sit amet, consectetur adipiscing elit. Donec ut neque nisi. Morbi non sem felis, sit amet pharetra leo. Vivamus vestibulum ultrices lacus non fringilla. Proin aliquet nisl vel metus semper euismod. Nam tincidunt blandit nisl, sit amet vulputate augue hendrerit vel. Integer faucibus, dolor sed lobortis rhoncus, felis dolor adipiscing enim, sed</p>
<a class="buy-now" href="#">Buy Now</a>

<div class="frame hero-frame">
  <div class="photo" role="img" aria-label="Black and white photo of a pair of worn minimal running shoes"></div>
  <svg class="ribbon" width="140" height="140" viewBox="0 0 140 140" style="top:-20px; right:-20px;">
    <polygon points="40,0 80,0 140,60 140,100" fill="var(--green)"/>
    <polygon points="140,100 140,110 130,100" fill="var(--green-dark)"/>
    <text x="98" y="48" fill="#ffffff" font-family="Roboto Condensed, sans-serif" font-style="italic" font-weight="700" font-size="17" text-anchor="middle" transform="rotate(45 98 48)">featured</text>
  </svg>
</div>

<h3 class="heading" style="left:204px; top:483px; font-size:15px;">Featured Products</h3>

<div class="frame thumb" style="left:204px;">
  <div class="photo" role="img" aria-label="Blue canvas sneakers"></div>
  <svg class="ribbon" width="60" height="60" viewBox="0 0 60 60" style="top:-8px; right:-8px;"><polygon points="18,0 34,0 60,26 60,42" fill="var(--green)"/></svg>
</div>
<div class="frame thumb" style="left:408px;">
  <div class="photo" role="img" aria-label="Worn grey running shoes"></div>
  <svg class="ribbon" width="60" height="60" viewBox="0 0 60 60" style="top:-8px; right:-8px;"><polygon points="18,0 34,0 60,26 60,42" fill="var(--green)"/></svg>
</div>
<div class="frame thumb" style="left:612px;">
  <div class="photo" role="img" aria-label="Pair of old muddy trainers"></div>
  <svg class="ribbon" width="60" height="60" viewBox="0 0 60 60" style="top:-8px; right:-8px;"><polygon points="18,0 34,0 60,26 60,42" fill="var(--green)"/></svg>
</div>
<div class="frame thumb" style="left:816px;">
  <div class="photo" role="img" aria-label="White running shoe with pink accents"></div>
  <svg class="ribbon" width="60" height="60" viewBox="0 0 60 60" style="top:-8px; right:-8px;"><polygon points="18,0 34,0 60,26 60,42" fill="var(--green)"/></svg>
</div>

<h2 class="heading" style="left:204px; top:655px; font-size:21px;">Welcome to Leap Fern Boots</h2>
<p class="copy" style="left:204px; top:693px; width:790px; height:90px; overflow:hidden;">Lorem ipsum dolor sit amet, consectetur adipiscing elit. Donec ut neque nisi. Morbi non sem felis, sit amet pharetra leo. Vivamus vestibulum ultrices lacus non fringilla. Proin aliquet nisl vel metus semper euismod. Nam tincidunt blandit nisl, sit amet vulputate augue hendrerit vel. Integer faucibus, dolor sed lobortis rhoncus, felis dolor adipiscing enim, sed Lorem ipsum dolor sit amet, consectetur adipiscing elit. Donec ut neque nisi. Morbi non sem felis, sit amet pharetra leo. Vivamus vestibulum ultrices lacus non fringilla. Proin aliquet nisl vel metus semper euismod. Nam tincidunt blandit nisl, sit amet vulputate augue hendrerit vel. Integer faucibus, dolor sed lobortis rhoncus felis dolor adipiscing enim, sed sollicitudin metus augue quis massa.</p>
<p class="copy" style="left:204px; top:811px; width:790px; height:45px; overflow:hidden;">Proin rhoncus tempus nisl, eu ullamcorper nunc pharetra in. Phasellus cursus augue vitae ante rhoncus ultrices. Proin tortor purus, bibendum non ultrices a, volutpat in tellus. Nam egestas porta risus, aliquet imperdiet enim scelerisque nec. Vivamus a elit id turpis auctor pellentesque nec ut justo. Vivamus dapibus ullamcorper nisi a adipiscing. Quisque eleifend vestibulum dui non semper. Aliquam aliquam sem odio, ac condimentum justo.</p>
<p class="copy" style="left:204px; top:888px; width:790px; height:15px; overflow:hidden;">Sed ut sapien dignissim ex lacinia auctor id accumsan nunc. Duis diam augue, faucibus eu luctus at, tempus ac dui. Lorem ipsum dolor sit amet, consectetur</p>

<footer class="site-footer">Copyright 2010 Leap Fern Boots All Rights Reserved</footer>

</body>
</html>
```